Broschüren-Design für gemeinnützige Organisation
Zielgruppe
Als gemeinnützige Organisation unterstützen wir Kinder und Jugendliche, vor allem in den Bereichen Schul- und Berufsausbildung. Wir arbeiten vorwiegend in Ostafrika, vor allem in Tansania und Kenia. Mit dieser Broschüre wollen wir für unser neues Pilotprojekt werben, den Aufbau eines dualen Ausbildungszentrums für junge Menschen in Kenia. Ziel des Ausbildungszentrums ist es jungen Menschen eine qualifizierte Berufsausbildung zu ermöglichen und damit Perspektiven und Zukunft im Heimatland.
Unsere Zielgruppe: Menschen mit Herz und Weitblick von 18 bis 80+
Aufgabenstellung
Die Broschüre sollte handlich sein und leicht zum einstecken. Derzeit haben wir den Text und die Gestaltung auf das Format DIN lang hoch (105x210 mm, 12 Seiten) ausgelegt. Ist aber nur ein Vorschlag und kein muss.
Die einzige Vorgabe ist das orange aus dem Logo mit der Farbe #ff3300 Ansonsten gibt es keine Vorgaben was Schrift, Farbgestaltung, Layout, Form, Seitenanzahl...ect betrifft. Allerdings sollte darauf geachtet werden, dass die Textinhalte der Doppelseiten erhalten bleiben (z.B. Seite 2 links - Seite 3 rechts, usw.)
Mitgeliefert werden Fotos, die gerne Verwendung finden können. Sollten aber weitere oder aussagekräftigere Fotos und Hintergründe benötigt werden, sind wir absolut offen dafür.

```html
<!DOCTYPE html>
<html lang="de">
<head>
<meta charset="utf-8">
<title>Broschüre – Die Herausforderung</title>
<link href="https://fonts.googleapis.com/css2?family=Ubuntu:wght@400;500;700&family=Roboto+Condensed:ital,wght@0,700;1,400&display=swap" rel="stylesheet">
<style>
  :root {
    --orange: #e85e1c;
    --text: #454545;
    --caption: #4a4a4a;
    --bg: #ffffff;
    --brand: #3b2a7a;
  }
  * { margin: 0; padding: 0; box-sizing: border-box; }
  html, body { width: 1200px; height: 2400px; overflow: hidden; background: var(--bg); }
  .page {
    position: relative;
    width: 1200px;
    height: 2400px;
    font-family: "Ubuntu", sans-serif;
    color: var(--text);
  }
  .section-title {
    position: absolute;
    left: 140px;
    font-family: "Ubuntu", sans-serif;
    font-weight: 700;
    font-size: 72px;
    line-height: 1;
    color: var(--orange);
    letter-spacing: 0.5px;
  }
  .body-text {
    position: absolute;
    left: 142px;
    width: 930px;
    font-size: 38px;
    line-height: 52px;
    color: var(--text);
  }
  .title-challenge { top: 124px; }
  .text-challenge { top: 240px; }
  .text-perspective { top: 490px; }
  .title-solution { top: 734px; }
  .text-solution { top: 848px; }
  .text-thanks { top: 1160px; }

  .portrait {
    position: absolute;
    left: 136px;
    top: 1336px;
    width: 1064px;
    height: 696px;
    background: linear-gradient(90deg, #3a3a3a 0%, #6b6b6b 28%, #a9a9a9 52%, #e6e6e6 72%, #ffffff 92%);
  }
  .portrait-caption {
    position: absolute;
    right: 44px;
    top: 1456px;
    width: 520px;
    text-align: right;
    font-family: "Roboto Condensed", sans-serif;
    color: var(--caption);
    font-size: 32px;
    line-height: 36px;
  }
  .portrait-caption .speaker { font-weight: 700; display: block; }
  .portrait-caption .quote { font-style: italic; display: block; }

  .brand {
    position: absolute;
    left: 0;
    top: 2160px;
    width: 1200px;
    display: flex;
    justify-content: center;
    align-items: center;
    gap: 18px;
    font-family: "Ubuntu", sans-serif;
    font-weight: 700;
    font-size: 38px;
    color: var(--brand);
  }
  .brand-mark { width: 40px; height: 40px; background: var(--brand); }
  .footer-rule {
    position: absolute;
    left: 0;
    top: 2258px;
    width: 1200px;
    height: 3px;
    background: var(--orange);
  }
</style>
</head>
<body>
<main class="page">
  <h2 class="section-title title-challenge">DIE HERAUSFORDERUNG</h2>
  <p class="body-text text-challenge">Eine duale Ausbildung gibt es nicht in Afrika. Über 70% der Jugendlichen haben deshalb keinen Zugang zu einer Berufsausbildung und damit keine Chance, dem Teufelsrad aus Elend und Armut zu entkommen.</p>
  <p class="body-text text-perspective">Ohne Perspektiven verlassen sie ihre Heimat, angezogen vom Leitstern Europa, auf der Suche nach einem besseren Leben.</p>

  <h2 class="section-title title-solution">DIE LÖSUNG</h2>
  <p class="body-text text-solution">Zukunft und Chance für junge Menschen in ihrer Heimat, durch Aufbau und qualifizierte Berufsausbildung in einem dualen Ausbildungs&shy;zentrum, das sich nach dem Aufbau selbst finanziert und hunderten Jugendlicher eine Berufsausbildung in ihrer Heimat ermöglicht.</p>
  <p class="body-text text-thanks">Wie Sie helfen können und auch unser „Dankeschön“ an Sie, erfahren Sie auf den nächsten Seiten.</p>

  <div class="portrait" role="img" aria-label="Schwarz-Weiß-Foto eines Jugendlichen, der mit einem Beutel über der Schulter auf einer Straße steht"></div>
  <p class="portrait-caption">
    <span class="speaker">Samuel, 17 Jahre, Tagelöhner</span>
    <span class="quote">„Ich schaue mich um in meiner Heimat und weiß, hier wird sich nichts für mich ändern. Nicht heute, nicht morgen. Ich habe nichts zu verlieren, also gehe ich.“</span>
  </p>

  <div class="brand"><span class="brand-mark"></span><span>brookwinkel</span></div>
  <div class="footer-rule"></div>
</main>
</body>
</html>
```